Business card for apparel company. Specializing in fishing and boating performance wear. Main company name is Marlow Pelican Company, LLC brand name for apparel is TIDEWAKE. See website www.TidewakeBayline.com I will attach some logos to consider.

```html
<!DOCTYPE html>
<html lang="en">
<head>
<meta charset="utf-8">
<title>Tidewake Business Card</title>
<link href="https://fonts.googleapis.com/css2?family=Arimo:wght@400;700&display=swap" rel="stylesheet">
<style>
  :root {
    --backdrop: #b9b9b9;
    --slate: #3d4d5e;
    --brand-blue: #1e9ad6;
    --paper: #ffffff;
    --ink-light: #e8edf2;
    --sea-glass: #9fc9c6;
  }
  * { margin: 0; padding: 0; box-sizing: border-box; }
  html, body { width: 1200px; height: 788px; overflow: hidden; }
  body {
    background: var(--backdrop);
    font-family: "Arimo", Arial, sans-serif;
    position: relative;
  }
  .card {
    position: absolute;
    top: 239px;
    width: 540px;
    height: 310px;
    border-radius: 18px;
    overflow: hidden;
    box-shadow: 0 10px 24px rgba(0,0,0,0.28);
  }
  .card--front { left: 45px; background: var(--paper); }
  .card--back { left: 615px; background: var(--slate); }
  .front-wave { position: absolute; inset: 0; width: 540px; height: 310px; }
  .brand-lockup {
    position: absolute;
    top: 26px;
    right: 62px;
    display: flex;
    align-items: center;
    gap: 10px;
  }
  .brand-mark {
    width: 22px; height: 22px;
    border-radius: 50%;
    background: var(--brand-blue);
  }
  .brand-name {
    font-weight: 700;
    font-size: 36px;
    line-height: 42px;
    letter-spacing: 1px;
    color: var(--brand-blue);
  }
  .contact {
    position: absolute;
    left: 34px;
    bottom: 22px;
    color: var(--ink-light);
  }
  .contact__name {
    font-weight: 700;
    font-size: 20px;
    line-height: 23px;
    color: var(--brand-blue);
    letter-spacing: 0.5px;
  }
  .contact__role { font-size: 14px; line-height: 16px; margin: 1px 0 8px; }
  .contact__list { list-style: none; font-size: 13.5px; }
  .contact__list li { display: flex; align-items: center; gap: 9px; line-height: 20px; }
  .contact__icon { width: 12px; height: 12px; flex: none; }
  .back-lockup {
    position: absolute;
    inset: 0;
    display: flex;
    align-items: center;
    justify-content: center;
    gap: 16px;
  }
  .back-mark {
    width: 40px; height: 40px;
    border-radius: 50%;
    border: 4px solid var(--sea-glass);
  }
  .back-name {
    font-weight: 700;
    font-size: 54px;
    letter-spacing: 2px;
    color: var(--sea-glass);
  }
</style>
</head>
<body>
  <section class="card card--front" aria-label="Business card front">
    <svg class="front-wave" viewBox="0 0 540 310" aria-hidden="true">
      <path d="M0,310 L0,188 C0,138 40,120 120,118 C300,113 440,98 540,48 L540,310 Z" fill="var(--brand-blue)"/>
      <path d="M0,310 L0,195 C0,145 40,127 120,125 C300,120 440,105 540,55 L540,310 Z" fill="var(--paper)"/>
      <path d="M0,310 L0,200 C0,150 40,132 120,130 C300,125 440,110 540,60 L540,310 Z" fill="var(--slate)"/>
    </svg>
    <div class="brand-lockup">
      <span class="brand-mark"></span>
      <span class="brand-name">TIDEWAKE</span>
    </div>
    <div class="contact">
      <p class="contact__name">CALDER REYES</p>
      <p class="contact__role">CEO/Founder</p>
      <ul class="contact__list">
        <li>
          <svg class="contact__icon" viewBox="0 0 12 12" aria-hidden="true"><path d="M2.5 1 L4.5 1 L5.2 3.5 L4 4.4 C4.7 6 6 7.3 7.6 8 L8.5 6.8 L11 7.5 L11 9.5 C11 10.3 10.3 11 9.5 11 C5 11 1 7 1 2.5 C1 1.7 1.7 1 2.5 1 Z" fill="var(--brand-blue)"/></svg>
          (123) 555-0148
        </li>
        <li>
          <svg class="contact__icon" viewBox="0 0 12 12" aria-hidden="true"><rect x="0.5" y="2.5" width="11" height="7.5" rx="1" fill="var(--brand-blue)"/><path d="M0.8 3 L6 7 L11.2 3" stroke="var(--slate)" stroke-width="1" fill="none"/></svg>
          info@TidewakeBayline.com
        </li>
        <li>
          <svg class="contact__icon" viewBox="0 0 12 12" aria-hidden="true"><circle cx="6" cy="6" r="5.2" fill="var(--brand-blue)"/><path d="M0.8 6 H11.2 M6 0.8 C3.5 3.5 3.5 8.5 6 11.2 M6 0.8 C8.5 3.5 8.5 8.5 6 11.2" stroke="var(--slate)" stroke-width="0.8" fill="none"/></svg>
          www.TidewakeBayline.com
        </li>
        <li>
          <svg class="contact__icon" viewBox="0 0 12 12" aria-hidden="true"><path d="M6 0.8 C3.6 0.8 2 2.6 2 4.7 C2 7.6 6 11.2 6 11.2 C6 11.2 10 7.6 10 4.7 C10 2.6 8.4 0.8 6 0.8 Z" fill="var(--brand-blue)"/><circle cx="6" cy="4.7" r="1.5" fill="var(--slate)"/></svg>
          Po Box 4120 Harbor Lane Country Name AB 3071
        </li>
      </ul>
    </div>
  </section>

  <section class="card card--back" aria-label="Business card back">
    <div class="back-lockup">
      <span class="back-mark"></span>
      <span class="back-name">TIDEWAKE</span>
    </div>
  </section>
</body>
</html>
```